" Atendimento médico em consultório/Clinica para mulheres em geral. A clinica contará com três médicas ginecologistas. Inicialmente somente a Dra. Lívia atenderá. O principal valor da Clinica é com o cuidado com a Mulher através de atendimento individual e cuidadoso através de especialistas nas áreas da ginecologia e Obstetricia. Apesar de possuir atendimento Obstétrico, o mesmo não será o principal foco da clinica. "

```html
<!DOCTYPE html>
<html lang="pt-BR">
<head>
<meta charset="UTF-8">
<title>Ginecologia Jardim – Cartão de visita</title>
<link href="https://fonts.googleapis.com/css2?family=Cormorant+Garamond:wght@400;500&family=Open+Sans:wght@400;600&display=swap" rel="stylesheet">
<style>
  :root{
    --coral:#ee6b6e;
    --coral-dark:#d9575b;
    --white:#ffffff;
    --ink:#6f6f6f;
    --backdrop:#efeae6;
  }
  *{margin:0;padding:0;box-sizing:border-box}
  html,body{width:1200px;height:1200px;overflow:hidden}
  body{
    background:var(--backdrop);
    display:flex;flex-direction:column;align-items:center;justify-content:center;gap:70px;
    font-family:"Open Sans",sans-serif;
  }
  .card{
    position:relative;width:900px;height:500px;border-radius:36px;overflow:hidden;
    box-shadow:0 12px 30px rgba(0,0,0,.12);
  }
  /* front */
  .card-front{background:var(--coral);color:var(--white);text-align:center}
  .brand-mark{
    position:absolute;left:50%;top:90px;transform:translateX(-50%);
    width:110px;height:110px;border:2px solid rgba(255,255,255,.85);border-radius:50%;
  }
  .brand-name{
    position:absolute;left:0;right:0;top:225px;
    font-family:"Cormorant Garamond",serif;font-weight:400;font-size:66px;letter-spacing:.5px;
  }
  .doctor-name{
    position:absolute;left:0;right:0;top:312px;
    font-family:"Cormorant Garamond",serif;font-size:30px;color:rgba(255,255,255,.9);
  }
  .front-tab{
    position:absolute;left:50%;bottom:0;transform:translateX(-50%);
    width:300px;height:48px;background:var(--white);border-radius:22px 22px 0 0;
  }
  /* back */
  .card-back{background:var(--white)}
  .back-tab{position:absolute;left:0;top:200px;width:22px;height:80px;background:var(--coral);border-radius:0 14px 14px 0}
  .back-title{
    position:absolute;left:70px;top:60px;
    font-family:"Cormorant Garamond",serif;font-size:44px;color:var(--coral);
  }
  .back-doctor{
    position:absolute;left:110px;top:112px;
    font-family:"Cormorant Garamond",serif;font-size:22px;color:var(--ink);
  }
  .contact-list{position:absolute;left:70px;top:190px;list-style:none;display:flex;flex-direction:column;gap:26px}
  .contact-item{display:flex;align-items:center;gap:18px;font-size:18px;color:var(--ink);line-height:1.4}
  .contact-icon{flex:none;width:38px;height:38px}
  .back-decoration{
    position:absolute;right:70px;top:70px;width:300px;height:300px;border-radius:50%;
    border:3px solid var(--coral);opacity:.35;
  }
</style>
</head>
<body>
  <section class="card card-front">
    <div class="brand-mark" role="img" aria-label="Área do símbolo da Ginecologia Jardim"></div>
    <h1 class="brand-name">Ginecologia Jardim</h1>
    <p class="doctor-name">Dra. Lívia Mori Sales</p>
    <div class="front-tab"></div>
  </section>

  <section class="card card-back">
    <div class="back-tab"></div>
    <h2 class="back-title">Ginecologia Jardim</h2>
    <p class="back-doctor">Dra. Lívia Mori Sales</p>
    <ul class="contact-list">
      <li class="contact-item">
        <svg class="contact-icon" viewBox="0 0 38 38" aria-hidden="true">
          <circle cx="19" cy="19" r="19" fill="var(--coral)"/>
          <path d="M13 11c1-1 2.5-1 3 0l1.6 3c.4.8 0 1.6-.6 2.1l-1 .8c.9 2 2.6 3.7 4.6 4.6l.8-1c.5-.6 1.3-1 2.1-.6l3 1.6c1 .5 1 2 0 3l-1.5 1.5c-1 1-2.6 1.2-4 .6-4.4-1.8-8-5.4-9.8-9.8-.6-1.4-.4-3 .6-4z" fill="#fff"/>
        </svg>
        <span>(19) 3000-0000<br>(19) 90000-0000</span>
      </li>
      <li class="contact-item">
        <svg class="contact-icon" viewBox="0 0 38 38" aria-hidden="true">
          <circle cx="19" cy="19" r="19" fill="var(--coral)"/>
          <rect x="10" y="13" width="18" height="12" rx="1.5" fill="none" stroke="#fff" stroke-width="2"/>
          <path d="M10.5 14l8.5 6.5 8.5-6.5" fill="none" stroke="#fff" stroke-width="2"/>
        </svg>
        <span>contato@ginecologiajardim.com.br<br>www.ginecologiajardim.com.br</span>
      </li>
      <li class="contact-item">
        <svg class="contact-icon" viewBox="0 0 38 38" aria-hidden="true">
          <circle cx="19" cy="19" r="19" fill="var(--coral)"/>
          <path d="M19 9a7 7 0 0 0-7 7c0 5.3 7 13 7 13s7-7.7 7-13a7 7 0 0 0-7-7z" fill="#fff"/>
          <circle cx="19" cy="16" r="2.6" fill="var(--coral)"/>
        </svg>
        <span>Rua das Flores, 120 - Centro<br>Cidade - SP - CEP 13000-000</span>
      </li>
    </ul>
    <div class="back-decoration" role="img" aria-label="Área decorativa do símbolo da marca"></div>
  </section>
</body>
</html>
```